Design a Product Label for a Natural Deodorant Product

This brief is for the development of a product label for a natural deodorant product that we are creating. The requirement is for a sticker label that will be applied to the package. Full details of the project are provided in the attached briefing document.

Target Market(s)

Those seeking an alternative to chemical laden deodorants. Interested in natural products with minimal waste etc.

Industry/Entity Type

Skin Care

Requirements
Must have
• On brand. Simple.

```html
<!DOCTYPE html>
<html lang="en">
<head>
<meta charset="utf-8">
<title>Halden Bay Natural Deodorant – Label</title>
<link href="https://fonts.googleapis.com/css2?family=Oswald:wght@500;600&display=swap" rel="stylesheet">
<style>
  :root {
    --bg: #e9eaec;
    --label: #ffffff;
    --sky: #6fc3dc;
    --sky-soft: #cbe9f2;
    --grey-text: #9a9ea3;
    --badge: #c9ccd1;
    --ink: #4a4f55;
  }
  * { box-sizing: border-box; margin: 0; padding: 0; }
  html, body { width: 1200px; height: 1200px; overflow: hidden; }
  body {
    background: var(--bg);
    font-family: "Oswald", sans-serif;
    position: relative;
  }
  .label {
    position: absolute;
    top: 300px;
    width: 500px;
    height: 600px;
    background: var(--label);
    overflow: hidden;
    box-shadow: 0 6px 24px rgba(0,0,0,0.08);
  }
  .label--front { left: 70px; }
  .label--back { left: 630px; }

  .wave-art {
    position: absolute;
    left: 0; top: 150px;
    width: 100%; height: 280px;
    background: linear-gradient(165deg,
      rgba(255,255,255,0) 0%,
      rgba(255,255,255,0) 28%,
      var(--sky-soft) 46%,
      var(--sky) 58%,
      var(--sky-soft) 66%,
      rgba(255,255,255,0) 82%);
    opacity: 0.7;
  }
  .brand {
    position: absolute;
    left: 0; right: 0; top: 82px;
    text-align: center;
    font-size: 72px;
    font-weight: 600;
    color: var(--grey-text);
    line-height: 1;
    letter-spacing: 1px;
  }
  .subtitle {
    position: absolute;
    left: 0; right: 0; top: 178px;
    text-align: center;
    font-size: 30px;
    font-weight: 600;
    color: var(--sky);
    letter-spacing: 0.5px;
    line-height: 1.2;
  }
  .net-weight {
    position: absolute;
    left: 50%; top: 430px;
    transform: translateX(-50%);
    width: 230px; height: 64px;
    background: var(--sky);
    border-radius: 10px;
    color: #fff;
    font-size: 28px;
    font-weight: 600;
    display: flex; align-items: center; justify-content: center;
    letter-spacing: 1px;
  }
  .badges {
    position: absolute;
    left: 0; right: 0; top: 525px;
    display: flex; justify-content: center; gap: 26px;
  }
  .badge {
    width: 46px; height: 46px;
    border-radius: 50%;
    background: var(--badge);
    border: 3px solid #fff;
    box-shadow: 0 0 0 2px var(--badge);
  }
  .info {
    position: absolute;
    left: 30px; right: 30px;
    font-size: 15px;
    font-weight: 500;
    color: var(--ink);
    line-height: 1.45;
  }
  .info h2 {
    font-size: 19px;
    font-weight: 600;
    color: var(--sky);
    margin-bottom: 4px;
  }
  .info--ingredients { top: 40px; }
  .info--directions { top: 175px; }
  .info em { font-style: normal; color: var(--sky); }
</style>
</head>
<body>
  <section class="label label--front">
    <div class="wave-art" role="img" aria-label="Flowing blue line wave decoration"></div>
    <h1 class="brand">Halden Bay</h1>
    <p class="subtitle">Natural Deodorant</p>
    <div class="net-weight">NTWT - 60g</div>
    <div class="badges">
      <span class="badge"></span><span class="badge"></span><span class="badge"></span><span class="badge"></span><span class="badge"></span>
    </div>
  </section>

  <section class="label label--back">
    <div class="wave-art" role="img" aria-label="Flowing blue line wave decoration"></div>
    <div class="info info--ingredients">
      <h2>Ingredients</h2>
      <p>Arrowroot powder, baking soda, coconut oil, shea butter, sweet almond oil, diatomaceous earth, essential oils (lemon mint).</p>
    </div>
    <div class="info info--directions">
      <h2>Directions</h2>
      <p><em>Halden Bay Natural Deodorant</em> is a gentle deodorant paste that keeps you fresh all day. Apply a small amount under arms and massage in softly. Store in a cool place out of direct sunlight. Use with clean, dry skin.</p>
    </div>
    <div class="net-weight">NTWT - 60g</div>
    <div class="badges">
      <span class="badge"></span><span class="badge"></span><span class="badge"></span><span class="badge"></span><span class="badge"></span>
    </div>
  </section>
</body>
</html>
```